Building business client journey document

We want to design a journey document which helps our clients understand the process of building a house from initial conversations through to construction. I have attached an example along with the design of stages/writing we would like for ours.

```html
<!DOCTYPE html>
<html lang="en">
<head>
<meta charset="utf-8">
<title>Client Journey – Initial Design Phase</title>
<link rel="stylesheet" href="https://fonts.googleapis.com/css2?family=Cabin:wght@400;500;600&display=swap">
<style>
  :root {
    --olive: #a9a67d;
    --olive-shadow: #8f8c66;
    --frame: #f4f4f4;
    --wall: #d3d4d6;
    --wall-light: #e2e3e4;
    --tile: #c6c7c9;
    --chimney: #c9cacc;
    --chimney-text: #8e8f92;
    --ink: #333336;
    --accent: #f5c518;
    --label: #111111;
    --label-text: #ffffff;
  }
  html, body {
    margin: 0;
    padding: 0;
    width: 1200px;
    height: 930px;
    overflow: hidden;
    background: var(--olive);
  }
  .journey {
    display: block;
    width: 1200px;
    height: 930px;
    font-family: "Cabin", "Gill Sans", sans-serif;
  }
  .phase-small { font-size: 24px; fill: var(--ink); font-weight: 400; }
  .phase-large { font-size: 40px; fill: var(--ink); font-weight: 400; letter-spacing: -0.5px; }
  .phase-tag { font-size: 24px; fill: var(--ink); font-weight: 500; }
  .chimney-text { font-size: 12.5px; fill: var(--chimney-text); letter-spacing: 0.3px; }
  .step-label { font-size: 8.5px; fill: var(--label-text); letter-spacing: 0.2px; }
  .step-label-tight { font-size: 7px; fill: var(--label-text); }
</style>
</head>
<body>
<svg class="journey" viewBox="0 0 672 521" preserveAspectRatio="none" xmlns="http://www.w3.org/2000/svg">
  <defs>
    <radialGradient id="wallGlow" cx="50%" cy="55%" r="65%">
      <stop offset="0%" stop-color="var(--wall-light)"/>
      <stop offset="100%" stop-color="var(--wall)"/>
    </radialGradient>
  </defs>

  <rect class="backdrop" width="672" height="521" fill="var(--olive)"/>

  <!-- house -->
  <polygon class="house-shadow" points="14,232 234,26 672,214 672,232 648,232 648,490 42,490 42,236" fill="var(--olive-shadow)" opacity="0.6"/>
  <polygon class="house-frame" points="8,224 228,18 665,205 665,224 640,224 640,482 36,482 36,228" fill="var(--frame)"/>
  <polygon class="house-wall" points="50,230 228,46 626,214 626,470 50,470" fill="url(#wallGlow)"/>

  <!-- chimney / details block -->
  <rect class="chimney" x="450" y="30" width="172" height="150" fill="var(--chimney)"/>
  <text class="chimney-text" x="535" y="88" text-anchor="middle">HEARTHLINE LOGO</text>
  <text class="chimney-text" x="535" y="106" text-anchor="middle">+ DETAILS</text>

  <!-- initial design phase heading -->
  <text class="phase-small" x="203" y="122">INITIAL</text>
  <text class="phase-large" x="172" y="157">Design</text>
  <rect class="phase-highlight" x="299" y="130" width="97" height="29" fill="var(--accent)"/>
  <text class="phase-tag" x="304" y="154">PHASE</text>

  <!-- dotted connector -->
  <g class="connector" fill="var(--ink)">
    <rect x="153" y="166" width="7" height="7"/>
    <rect x="180" y="166" width="7" height="7"/>
    <rect x="207" y="166" width="7" height="7"/>
    <rect x="234" y="166" width="7" height="7"/>
    <rect x="261" y="166" width="7" height="7"/>
    <rect x="288" y="166" width="7" height="7"/>
    <rect x="315" y="166" width="7" height="7"/>
    <rect x="342" y="166" width="7" height="7"/>
    <rect x="369" y="166" width="7" height="7"/>
    <rect x="396" y="166" width="7" height="7"/>
    <rect x="424" y="153" width="7" height="7"/>
    <rect x="142" y="187" width="7" height="7"/>
  </g>

  <!-- step 1: initial contact -->
  <g class="step step-contact">
    <rect class="step-tile" x="74" y="196" width="136" height="96" rx="12" fill="var(--tile)"/>
    <path class="step-frame" d="M88,205 H182 Q200,205 200,223 V259 Q200,277 182,277 H106 Q92,277 92,263 V220" fill="none" stroke="var(--accent)" stroke-width="5" stroke-linecap="round"/>
    <path class="icon-phone" d="M133,226 l7,-3 l6,11 l-5,4 q2,8 9,15 l5,-4 l10,7 l-3,7 q-14,2 -25,-14 q-8,-12 -4,-23 z" fill="var(--label)"/>
    <rect class="step-label-box" x="104" y="282" width="78" height="28" fill="var(--label)"/>
    <text class="step-label" x="143" y="294" text-anchor="middle">INITIAL</text>
    <text class="step-label" x="143" y="305" text-anchor="middle">CONTACT</text>
  </g>

  <polygon class="step-arrow" points="226,228 244,237 226,246" fill="var(--accent)"/>

  <!-- step 2: initial face to face -->
  <g class="step step-meeting">
    <rect class="step-tile" x="261" y="196" width="138" height="96" rx="12" fill="var(--tile)"/>
    <path class="step-frame" d="M276,205 H370 Q388,205 388,223 V259 Q388,277 370,277 H294 Q280,277 280,263 V220" fill="none" stroke="var(--accent)" stroke-width="5" stroke-linecap="round"/>
    <rect class="step-label-box" x="291" y="282" width="86" height="28" fill="var(--label)"/>
    <text class="step-label" x="334" y="294" text-anchor="middle">INITIAL</text>
    <text class="step-label" x="334" y="305" text-anchor="middle">FACE TO FACE</text>
  </g>

  <polygon class="step-arrow" points="414,228 432,237 414,246" fill="var(--accent)"/>

  <!-- step 3: estimate -->
  <g class="step step-estimate">
    <rect class="step-tile" x="449" y="196" width="138" height="96" rx="12" fill="var(--tile)"/>
    <path class="step-frame" d="M464,205 H558 Q576,205 576,223 V259 Q576,277 558,277 H482 Q468,277 468,263 V220" fill="none" stroke="var(--accent)" stroke-width="5" stroke-linecap="round"/>
    <rect class="step-label-box" x="478" y="282" width="86" height="28" fill="var(--label)"/>
    <text class="step-label-tight" x="521" y="294" text-anchor="middle">IST. BASE PAIDS</text>
    <text class="step-label-tight" x="521" y="304" text-anchor="middle">ESTIMATE</text>
  </g>

  <!-- preliminary phase heading -->
  <text class="phase-large" x="196" y="412">Preliminary</text>
  <rect class="phase-highlight" x="408" y="386" width="97" height="29" fill="var(--accent)"/>
  <text class="phase-tag" x="412" y="410">PHASE</text>
</svg>
</body>
</html>
```